Business Card Design Project

We need a business card for our IT services provider business. We provide services to small and medium business, and would like something that reflects the color scheme / branding on our recently updated website - www.larkbyte.com.au

The card type we have chosen is a matte laminated double sided configuration at 86mm x 54mm on 350 GSM cardboard.
Updates

Target Market(s)

Small and Medium Business owners

Industry/Entity Type

Business

Requirements
Must have
• *Details on all cards*

Company Name: LarkByte IT Pty Ltd
ABN: 62 385 219 604
Address: 47-49 Marrow Street, Kelbrook Vale, Eastwold 5812
Phone: 1300 LARK BY
Fax: 03 9417 6209
Website: www.larkbyte.com.au
Logo/Handprint Icon

*Person Specific*

```html
<!DOCTYPE html>
<html lang="en">
<head>
<meta charset="utf-8">
<title>LarkByte IT – Business Card</title>
<link href="https://fonts.googleapis.com/css2?family=Open+Sans:wght@300;400;600&family=Oswald:wght@700&display=swap" rel="stylesheet">
<style>
  :root {
    --backdrop: #3a3a3c;
    --card-dark: #2a2a2b;
    --card-blue: #3c7aa5;
    --band-blue: #3b7cab;
    --band-dark: #262627;
    --text-light: #f1f1f1;
    --text-muted: #cfcfcf;
    --logo-grey: #d9d9d9;
    --logo-dark: #2e2e30;
    --tagline-blue: #7fb6dc;
  }
  * { box-sizing: border-box; margin: 0; padding: 0; }
  html, body {
    width: 1200px; height: 900px; overflow: hidden;
    background: var(--backdrop);
  }
  .canvas {
    width: 1200px; height: 900px;
    display: flex; align-items: center; justify-content: center; gap: 60px;
  }
  .card {
    position: relative; width: 520px; height: 327px;
    overflow: hidden; border-radius: 2px;
    box-shadow: 0 10px 30px rgba(0,0,0,.35);
  }
  .card--front { background: var(--card-dark); }
  .card--back  { background: var(--card-blue); }
  .card__bands { position: absolute; inset: 0; width: 100%; height: 100%; }

  .contact {
    position: absolute; left: 38px; top: 34px;
    font-family: "Open Sans", sans-serif; color: var(--text-muted);
    font-size: 10.5px; line-height: 1.55;
  }
  .contact__name {
    font-family: "Oswald", sans-serif; font-weight: 700;
    font-size: 22px; color: var(--text-light); line-height: 1.2;
  }
  .contact__role { margin-bottom: 8px; }
  .contact__lines { margin-bottom: 8px; }
  .contact__company { font-weight: 600; color: var(--text-light); }

  .wordmark {
    position: absolute; font-family: "Open Sans", sans-serif;
    text-align: right; white-space: nowrap;
  }
  .wordmark__name { font-weight: 300; line-height: 1; display: flex; align-items: center; justify-content: flex-end; gap: 8px; }
  .wordmark__dot { display: inline-block; border-radius: 50%; }
  .wordmark__tagline { font-weight: 400; margin-top: 4px; }

  .card--front .wordmark { right: 48px; bottom: 34px; }
  .card--front .wordmark__name { font-size: 34px; color: var(--logo-grey); }
  .card--front .wordmark__dot { width: 12px; height: 12px; background: var(--band-blue); }
  .card--front .wordmark__tagline { font-size: 11px; color: var(--tagline-blue); }

  .card--back .wordmark { left: 50%; top: 50%; transform: translate(-50%, -50%); }
  .card--back .wordmark__name { font-size: 46px; color: var(--logo-dark); }
  .card--back .wordmark__dot { width: 14px; height: 14px; background: var(--text-light); }
  .card--back .wordmark__tagline { font-size: 14px; color: var(--text-light); }
</style>
</head>
<body>
<main class="canvas">
  <section class="card card--front" aria-label="Business card front">
    <svg class="card__bands" viewBox="0 0 520 327" aria-hidden="true">
      <path fill="var(--band-blue)" d="M30,0 C52,0 56,15 86,15 H434 C464,15 468,0 490,0 Z"/>
      <path fill="var(--band-blue)" d="M30,327 C52,327 56,312 86,312 H434 C464,312 468,327 490,327 Z"/>
    </svg>
    <div class="contact">
      <p class="contact__name">Marcus Delaney</p>
      <p class="contact__role">Managing Director</p>
      <div class="contact__lines">
        <p>Mobile: +1 58 72 30 46</p>
        <p>Email: contact@larkbyte.com.au</p>
        <p>Tel: 1300 LARK BY</p>
        <p>Fax: 03 9417 6209</p>
        <p>Web: www.larkbyte.com.au</p>
      </div>
      <p class="contact__company">LarkByte IT Pty Ltd</p>
      <p>47-49 Marrow Street, Kelbrook Vale, Eastwold 5812</p>
    </div>
    <div class="wordmark">
      <p class="wordmark__name"><span class="wordmark__dot"></span>LarkByte IT</p>
      <p class="wordmark__tagline">Systems, Sorted Smartly!</p>
    </div>
  </section>

  <section class="card card--back" aria-label="Business card back">
    <svg class="card__bands" viewBox="0 0 520 327" aria-hidden="true">
      <path fill="var(--band-dark)" d="M30,0 C52,0 56,18 86,18 H434 C464,18 468,0 490,0 Z"/>
      <path fill="var(--band-dark)" d="M30,327 C52,327 56,309 86,309 H434 C464,309 468,327 490,327 Z"/>
    </svg>
    <div class="wordmark">
      <p class="wordmark__name"><span class="wordmark__dot"></span>LarkByte IT</p>
      <p class="wordmark__tagline">Systems, Sorted Smartly!</p>
    </div>
  </section>
</main>
</body>
</html>
```